Business Cards for our company

Hi there,

we have successfully designed a logo with ArtFlock and would like now to design our business cards. We would like to keep the colours and the look-and-feel of the logo. Please send in variations with two or three colours and one or two sides. I promise to respond to every single submission.

Many thanks and happy new year.

All the best,
Wilfried

Target Market(s)

B2B

Industry/Entity Type

Trade

Contact Information for Business Card

We have successfully designed a logo with ArtFlock and would like now to design our business cards. We would like to keep the colours and the look-and-feel of the logo. Please send in variations with two or three colours and one or two sides. I promise to respond to every single submission.

Font styles to use
Serif
Sans Serif
Script

Requirements
Must have
• These information should be on the business card, grouped as you suggest, and we think using small pictograms for mobile, email, etc is pretty helpful:
• Wilfried Tammler (first and second name)
• Geschäftsführer/ Managing Director (title)
• KoR Warenkontor GmbH (company name and legal form)
• Ostheimer Str. 18/3 (street and house number)
• 70839 Gerlingen (zip code and town)
• +491709384562 (mobile)
• +4971569027341 (work)
• w.tammler@kor-warenkontor.example (email)
• www.kor-warenkontor.example (web)
Nice to have
• Spectacular and interesting layout and design. You look at it and think, wow, that's not the normal stuff.
• We think of ourselves as bridge-builders between businesses (international producers on the one hand, and retail chains on the other hand) and we translate, organise and manage projects where both partners are involved, but it's difficult for them to cooperate due to language barriers and different working cultures.
• This is why we have the n between the B's shaped as a bridge, and the green arc supports this idea. Maybe you could play with this idea...
Should not have
• the standard layout that everybody has

```html
<!DOCTYPE html>
<html lang="en">
<head>
<meta charset="utf-8">
<title>KoR Warenkontor – Business Card</title>
<link rel="stylesheet" href="https://fonts.googleapis.com/css2?family=Arimo:wght@400;700&display=swap">
<style>
  :root {
    --backdrop: #6e6a6a;
    --card: #ffffff;
    --ink: #111111;
    --green: #2eaa4a;
    --mark-grey: #8a8a8a;
    --divider: rgba(50, 50, 50, 0.6);
  }
  html, body {
    margin: 0;
    padding: 0;
    width: 1200px;
    height: 873px;
    overflow: hidden;
    background: var(--backdrop);
    font-family: "Arimo", Arial, sans-serif;
  }
  .stage {
    position: relative;
    width: 1200px;
    height: 873px;
  }
  .card {
    position: absolute;
    left: 147px;
    top: 212px;
    width: 963px;
    height: 286px;
    background: var(--card);
  }
  .wordmark {
    position: absolute;
    left: 25px;
    top: 16px;
    margin: 0;
    color: var(--ink);
    font-weight: 700;
    font-size: 34px;
    line-height: 1.05;
  }
  .wordmark span { display: block; font-size: 15px; letter-spacing: 0.5px; }
  .holder {
    position: absolute;
    left: 24px;
    top: 124px;
  }
  .holder-name {
    margin: 0;
    color: var(--green);
    font-size: 18px;
    font-weight: 400;
    line-height: 22px;
    text-transform: uppercase;
  }
  .holder-title {
    margin: 2px 0 0 3px;
    font-size: 13px;
    line-height: 16px;
    color: var(--ink);
  }
  .contacts {
    position: absolute;
    left: 24px;
    top: 196px;
    margin: 0;
    padding: 0;
    list-style: none;
    font-size: 11px;
    color: var(--ink);
  }
  .contacts li {
    display: flex;
    align-items: flex-start;
    gap: 8px;
    line-height: 12px;
    margin-bottom: 5px;
  }
  .contacts svg { width: 12px; height: 12px; flex: none; }
  .feature-mark {
    position: absolute;
    left: 298px;
    top: 32px;
    width: 365px;
    margin: 0;
    color: var(--mark-grey);
    font-weight: 700;
    text-align: center;
    line-height: 1;
  }
  .feature-mark .big { display: block; font-size: 170px; letter-spacing: -3px; }
  .feature-mark .sub { display: block; font-size: 40px; margin-top: 16px; letter-spacing: 2px; }
  .web {
    position: absolute;
    right: 16px;
    top: 108px;
  }
  .web-address {
    margin: 0;
    font-size: 18px;
    font-weight: 700;
    color: var(--ink);
  }
  .web-address .domain { color: var(--green); }
  .tagline {
    margin: 6px 0 0;
    font-size: 13px;
    font-weight: 700;
    color: var(--ink);
  }
  .fold-line {
    position: absolute;
    left: 626px;
    top: 140px;
    width: 5px;
    height: 435px;
    background: var(--divider);
  }
</style>
</head>
<body>
<div class="stage">
  <section class="card">
    <p class="wordmark">KoR<span>Warenkontor GmbH</span></p>

    <div class="holder">
      <h1 class="holder-name">Wilfried Tammler</h1>
      <p class="holder-title">Geschäftsführer / Managing Director</p>
    </div>

    <ul class="contacts">
      <li>
        <svg viewBox="0 0 13 13" aria-hidden="true"><rect x="3" y="0.5" width="7" height="12" rx="1" fill="none" stroke="var(--green)" stroke-width="1.3"/></svg>
        +491709384562
      </li>
      <li>
        <svg viewBox="0 0 13 13" aria-hidden="true"><path d="M1 5 Q6.5 1 12 5 L10.5 6.5 L9 5.5 L4 5.5 L2.5 6.5 Z" fill="var(--green)"/><rect x="3" y="7" width="7" height="5" rx="1" fill="var(--green)"/></svg>
        +4971569027341
      </li>
      <li>
        <svg viewBox="0 0 13 13" aria-hidden="true"><rect x="0.5" y="2.5" width="12" height="8" fill="var(--green)"/><path d="M0.5 2.5 L6.5 7 L12.5 2.5" fill="none" stroke="#fff" stroke-width="1"/></svg>
        w.tammler@kor-warenkontor.example
      </li>
      <li>
        <svg viewBox="0 0 13 13" aria-hidden="true"><path d="M6.5 0.5 A4 4 0 0 1 10.5 4.5 C10.5 7.5 6.5 12.5 6.5 12.5 C6.5 12.5 2.5 7.5 2.5 4.5 A4 4 0 0 1 6.5 0.5 Z" fill="var(--green)"/><circle cx="6.5" cy="4.5" r="1.5" fill="#fff"/></svg>
        <span>Ostheimer Str. 18/3<br>70839 Gerlingen</span>
      </li>
    </ul>

    <p class="feature-mark" aria-hidden="true"><span class="big">KoR</span><span class="sub">Warenkontor</span></p>

    <div class="web">
      <p class="web-address">www.<span class="domain">kor-warenkontor</span>.example</p>
      <p class="tagline">bridge-builders between businesses</p>
    </div>
  </section>
  <div class="fold-line"></div>
</div>
</body>
</html>
```